Marrowfield Realty

Business cards for 4 people

They need to say for all
87 Tamsin Quay, Boston MA 02118

Each person will have their own personal information
We would like gold embossing for the name of the company
Priya is the blonde sitting in the chair smiling her information should be on the back of the card with her name and information
Should say for slogan Timeless Homes, Considered Service
priya@marrowfieldhomes.com
(413) 555-0172

Dorota is the brunette with wavy hair in the tan suit dorota@marrowfieldhomes.com
(617) 555-0193

ines@marrowfieldhomes.com
(413) 555-0148
standing next to the chair

leda@marrowfieldhomes.com
(413) 555-0161
close up headshot

```html
<!DOCTYPE html>
<html lang="en">
<head>
<meta charset="utf-8">
<title>Marrowfield Realty – Business Cards</title>
<link href="https://fonts.googleapis.com/css2?family=Cinzel:wght@600&family=Lato:wght@400&display=swap" rel="stylesheet">
<style>
  :root {
    --navy: #1c2d50;
    --navy-deep: #0d1a36;
    --navy-light: #223762;
    --gold: #d4a545;
    --gold-light: #f0d27a;
    --gold-dark: #a57a26;
    --ink-light: #f3f1ec;
    --photo-grey: #d9d9d4;
    --photo-tan: #a88563;
    --page: #e6e4df;
  }
  * { box-sizing: border-box; margin: 0; padding: 0; }
  html, body { width: 1200px; height: 900px; overflow: hidden; }
  body {
    background: var(--page);
    font-family: "Lato", sans-serif;
    display: flex;
    flex-direction: column;
    align-items: center;
    justify-content: center;
    gap: 40px;
  }
  .card {
    width: 700px;
    height: 400px;
    border-radius: 4px;
    overflow: hidden;
    box-shadow: 0 10px 28px rgba(0,0,0,0.22);
  }

  /* Front side */
  .card-front { display: flex; background: var(--navy); }
  .portrait {
    width: 300px;
    height: 100%;
    flex: none;
    background: radial-gradient(ellipse 45% 55% at 55% 55%, var(--photo-tan) 0%, rgba(168,133,99,0.35) 60%, transparent 100%), var(--photo-grey);
  }
  .gold-divider {
    width: 9px;
    flex: none;
    background: linear-gradient(90deg, var(--gold-dark), var(--gold-light), var(--gold-dark));
  }
  .details {
    flex: 1;
    padding: 44px 36px 30px 44px;
    background: linear-gradient(160deg, var(--navy-light), var(--navy));
    color: var(--ink-light);
    display: flex;
    flex-direction: column;
  }
  .brand-name {
    font-family: "Cinzel", serif;
    font-weight: 600;
    color: var(--gold);
    font-size: 26px;
    letter-spacing: 1px;
    line-height: 1.1;
    text-align: center;
    margin-bottom: 40px;
  }
  .person-name {
    font-family: "Cinzel", serif;
    font-weight: 600;
    color: var(--gold);
    font-size: 17px;
    letter-spacing: 1px;
  }
  .person-title { font-size: 15px; margin-bottom: 18px; }
  .contact-list { list-style: none; font-size: 15px; line-height: 1.75; }
  .contact-list li { display: flex; align-items: center; gap: 10px; }
  .contact-list svg { width: 16px; height: 16px; flex: none; }
  .rule { height: 2px; background: var(--gold); margin: 8px 0; width: 86%; }
  .slogan { font-size: 15px; letter-spacing: 0.3px; }

  /* Back side */
  .card-back {
    background: radial-gradient(ellipse at 50% 45%, var(--navy-light) 0%, var(--navy-deep) 75%);
    display: flex;
    align-items: center;
    justify-content: center;
  }
  .card-back .brand-name { font-size: 44px; letter-spacing: 2px; margin: 0; }
</style>
</head>
<body>
  <section class="card card-front">
    <div class="portrait" role="img" aria-label="Photo of Dorota seated on a wooden chair in a tan suit"></div>
    <div class="gold-divider"></div>
    <div class="details">
      <div class="brand-name">Marrowfield Realty</div>
      <div class="person-name">DOROTA VELLACOURT</div>
      <div class="person-title">Real Estate Advisor and Sales Manager</div>
      <ul class="contact-list">
        <li>
          <svg viewBox="0 0 16 16" aria-hidden="true"><rect x="4" y="1" width="8" height="14" rx="1.5" fill="none" stroke="#d4a545" stroke-width="1.5"/><line x1="7" y1="12.5" x2="9" y2="12.5" stroke="#d4a545" stroke-width="1.5"/></svg>
          (617) 555-0193
        </li>
        <li>
          <svg viewBox="0 0 16 16" aria-hidden="true"><rect x="1" y="3" width="14" height="10" fill="#d4a545"/><polyline points="1,3 8,9 15,3" fill="none" stroke="#1c2d50" stroke-width="1.3"/></svg>
          dorota@marrowfieldhomes.com
        </li>
        <li>87 Tamsin Quay, Boston MA 02118</li>
      </ul>
      <div class="rule"></div>
      <div class="slogan">Timeless Homes, Considered Service</div>
    </div>
  </section>

  <section class="card card-back">
    <div class="brand-name">Marrowfield Realty</div>
  </section>
</body>
</html>
```